facelift of our car wrap design - for Varno Klido L2

We would like to give our vehicles a facelift. Attached is our current advertising material.
Must-have: The paintwork of our vehicles is and will remain yellow. I would prefer to use the newer company logo, without the coloured bars, as shown in the attachment.
You can find further inspiration at www.plimtaaab.ch.

it should be a classic new design

• some advertising keywords

```html
<!DOCTYPE html>
<html lang="de">
<head>
<meta charset="utf-8">
<title>PLIMTAAAB – Fahrzeugbeschriftung Varno Klido L2</title>
<link rel="stylesheet" href="https://fonts.googleapis.com/css2?family=Montserrat:wght@600;800&display=swap">
<style>
  :root {
    --paint-yellow: #f7cf1b;
    --ink: #161616;
    --canvas: #ffffff;
  }
  * { margin: 0; padding: 0; box-sizing: border-box; }
  html, body { width: 1200px; height: 715px; overflow: hidden; background: var(--canvas); }
  body { font-family: "Montserrat", sans-serif; color: var(--ink); }
  .sheet { position: relative; width: 1200px; height: 715px; }

  .panel { position: absolute; background: var(--paint-yellow); border-radius: 18px; }
  .panel--rear { left: 110px; top: 55px; width: 233px; height: 175px; border-radius: 16px 16px 6px 6px; }
  .panel--side-right { left: 405px; top: 57px; width: 699px; height: 200px; border-radius: 14px 60px 40px 14px; }
  .panel--side-left { left: 395px; top: 295px; width: 657px; height: 200px; border-radius: 60px 14px 14px 40px; }
  .panel--roof { left: 461px; top: 533px; width: 507px; height: 132px; border-radius: 40px 14px 14px 40px; }

  .wordmark { position: absolute; font-weight: 800; letter-spacing: 0.5px; line-height: 1; white-space: nowrap; }
  .claim { position: absolute; font-weight: 600; letter-spacing: 2.6px; white-space: nowrap; line-height: 1; }

  .services { position: absolute; list-style: none; font-weight: 600; line-height: 1; }
  .services li { display: flex; align-items: center; white-space: nowrap; }
  .services li::before { content: ""; display: inline-block; border: 1.4px solid var(--ink); border-radius: 50%; }

  /* rear */
  .panel--rear .wordmark { left: 43px; top: 26px; font-size: 17px; }
  .panel--rear .claim { left: 43px; top: 48px; font-size: 5.6px; letter-spacing: 1.6px; }
  .panel--rear .services { left: 32px; top: 70px; font-size: 6px; }
  .panel--rear .services li { height: 12.6px; }
  .panel--rear .services li::before { width: 6px; height: 6px; margin-right: 7px; }
  .values { position: absolute; left: 141px; top: 101px; font-size: 7.4px; font-weight: 600; line-height: 12.6px; letter-spacing: 0.3px; }
  .values::after { content: ""; display: block; width: 22px; height: 1.4px; background: var(--ink); margin-top: 6px; }
  .web { position: absolute; left: 0; width: 100%; top: 156px; text-align: center; font-size: 9.4px; font-weight: 600; }

  /* sides */
  .panel--side-right .wordmark { left: 60px; top: 40px; font-size: 27px; }
  .panel--side-right .claim { left: 60px; top: 67px; font-size: 8.2px; }
  .panel--side-right .services { left: 311px; top: 29px; }
  .panel--side-left .wordmark { left: 313px; top: 37px; font-size: 27px; }
  .panel--side-left .claim { left: 313px; top: 64px; font-size: 8.2px; }
  .panel--side-left .services { left: 537px; top: 24px; }
  .panel--side-right .services, .panel--side-left .services { font-size: 7.8px; }
  .panel--side-right .services li, .panel--side-left .services li { height: 15.5px; }
  .panel--side-right .services li::before, .panel--side-left .services li::before { width: 8px; height: 8px; margin-right: 9px; }

  /* roof */
  .roof-mark { position: absolute; left: 60px; top: 8px; transform-origin: top left; transform: translateX(0) rotate(90deg); }
  .roof-mark .wordmark { position: static; font-size: 14px; display: block; }
  .roof-mark .claim { position: static; font-size: 3.6px; letter-spacing: 1.2px; display: block; margin-top: 3px; }
  .roof-windscreen { position: absolute; left: 70px; top: 10px; width: 72px; height: 112px; background: #2b2b2b; border-radius: 30px 8px 8px 30px; }
</style>
</head>
<body>
<main class="sheet">

  <section class="panel panel--rear" aria-label="Heckansicht">
    <div class="wordmark">PLIMTAAAB</div>
    <div class="claim">HAUSTECHNIK + BAUSPENGLEREI</div>
    <ul class="services">
      <li>HEIZUNG</li><li>SANITÄR</li><li>LÜFTUNG</li><li>SPENGLEREI</li><li>DACH &amp; FASSADE</li>
    </ul>
    <p class="values">QUALITÄT.<br>PRÄZISION.<br>ZUVERLÄSSIG.</p>
    <p class="web">plimtaaab.ch</p>
  </section>

  <section class="panel panel--side-right" aria-label="Beifahrerseite">
    <div class="wordmark">PLIMTAAAB</div>
    <div class="claim">HAUSTECHNIK + BAUSPENGLEREI</div>
    <ul class="services">
      <li>HEIZUNG</li><li>SANITÄR</li><li>LÜFTUNG</li><li>SPENGLEREI</li><li>DACH &amp; FASSADE</li>
    </ul>
  </section>

  <section class="panel panel--side-left" aria-label="Fahrerseite">
    <div class="wordmark">PLIMTAAAB</div>
    <div class="claim">HAUSTECHNIK + BAUSPENGLEREI</div>
    <ul class="services">
      <li>HEIZUNG</li><li>SANITÄR</li><li>LÜFTUNG</li><li>SPENGLEREI</li><li>DACH &amp; FASSADE</li>
    </ul>
  </section>

  <section class="panel panel--roof" aria-label="Dachansicht">
    <div class="roof-mark">
      <span class="wordmark">PLIMTAAAB</span>
      <span class="claim">HAUSTECHNIK + BAUSPENGLEREI</span>
    </div>
    <div class="roof-windscreen" role="img" aria-label="Windschutzscheibe von oben"></div>
  </section>

</main>
</body>
</html>
```